Wine Label Design-Crimson Gully Vineyard

Crimson Gully Vineyard is in the Barossa Valley in South Australia. The Barossa is recognized as Australia's premier wine region, producing Australia's icon wines and some " new takes on traditional".
This family owned and operated vineyard grows some exceptionally high quality fruit. Most of the fruit is sold and used for some of Australia's most iconic wines. Small quantities are retained by the owners for some wines with very limited availability. (Wines were previously sold as Pellow Draycott Vineyards Crimson Gully ( Shiraz, Cabernet etc).

The wines will in the future be labeled simply ‘Crimson Gully Vineyard’. The label will launch this new identity for the single family single vineyard and its high quality wines which are a true expression of the vineyard and derive from the Crimson Gully common to this ancient area (800-2000 million years old).
The label should reflect
• Single vineyard, family owned
• vines in very old rock & soils
• High quality & reliability
• Edgy but true, design based thinking (Please note:blue is generally seen as an unacceptable colour for a wine label?? Don’t ask me why)

The wines will be sold mostly direct in Australia ( ie not through retail stores), with limited export to Asia, Scandinavia and Canada.
There are three quality levels and price points in the portfolio
1. Entry level premium for everyday drinking for discriminating drinkers-approx AUD20
2. Super Premium-approx AUD30
3. Limited Release ultlra premium-AUD75-90?
We envisage three variations on the label but with an obvious & common design element. This design element should be able to be used for corporate identification and promotion
The paper stock will be waterproof and self adhesive. Our preference is for designs that engage the user by appealing to both sight and touch. It is preferred that textures be added eg embossing, high build varnish etc-rather than be a facet of the stock itself.
For information on statutory label requirements refer to www.vintnerregistry-example.com . In brief
o Front label need not show any mandatory information. However we would prefer Variety, Barossa Valley, Year and alcohol to be shown on the front label
o Back label should show all mandatories and allow for a bar code

Project Deadline Extended
Reason: I've had a problem with my wireless broadband account and reception has been intermittent to say the least to the extent that I switched off at the weekend. Just going downtown now for a 'polite discussion' with my service provider.

Project Deadline Extended
Reason: I have receiver insufficient designs of quality which we would consider. Too many designs have a "cut and paste" appearance - too few exhibit an original art/design element which truly identifies the product.

Gals & Guys

most of the designs submitted lack punch and originality and are totally unmemorable.
Please-get on Google or whatever enter "Wine Label Designs" and do some research b4 u waste your time and mine. Formulaic cut and paste will not win the day. That's not to say that cut and paste can't work-but it must have some originality, impact and command attention. Please surprise me.

Following on from a question from a designer about who is our competition and what we are looking for I sent the following 
"I don't think I can add anything new. Read the brief and comments again and research wine labels on the web. In 30 minutes you'll get a good idea of the creative edgy designs in the industry. There are a plethora of collections. Our competition-anyone with a label. In 2010 there were over 2400 "producers" in other words 2400 producers with at least one label. In fact there are over 25000 Australian wines and then the numerous imported wines.

Target Market(s)

$20 people who budget everyday but have graduated from drinking 'entry level' wines. These people will likely fit into Cat. (b) in the $30 wine

$30 (a) will not over-compromise on some everyday discretionary expenditure.(b) might buy for special occasions

$70-$90 Professional/successful people with high disposable/discretionary income not particularly worried about recession. wine geeks.

Industry/Entity Type

Retail

Requirements
Must have
• identifiable element across range of wines

```html
<!DOCTYPE html>
<html lang="en">
<head>
<meta charset="utf-8">
<title>Crimson Gully Vineyard – Front Label</title>
<link rel="stylesheet" href="https://fonts.googleapis.com/css2?family=Tinos&display=swap">
<style>
  :root {
    --backdrop: #e6e6e6;
    --wood: #b38c58;
    --wood-dark: #9c7645;
    --paper: #efe6d1;
    --plum: #4b2f3b;
    --frame: #5b3c22;
    --ink: #1c1712;
    --rock-dark: #3a3127;
    --rock-mid: #8a7150;
    --rock-light: #a68a62;
  }
  * { margin: 0; padding: 0; box-sizing: border-box; }
  html, body {
    width: 1200px; height: 1200px; overflow: hidden;
    background: var(--backdrop);
  }
  .label {
    position: absolute;
    left: 234px; top: 110px;
    width: 732px; height: 980px;
    background: var(--paper);
    overflow: hidden;
  }
  .wood-band {
    position: absolute; left: 0; width: 100%;
    background: linear-gradient(90deg, var(--wood) 0%, var(--wood-dark) 50%, var(--wood) 100%);
  }
  .wood-band--top { top: 0; height: 192px; }
  .wood-band--bottom { top: 881px; height: 99px; }
  .plum-stripe {
    position: absolute; left: 0; width: 100%;
    background: var(--plum);
  }
  .plum-stripe--top { top: 192px; height: 37px; }
  .plum-stripe--bottom { top: 863px; height: 18px; }
  .vineyard-panel {
    position: absolute;
    left: 114px; top: 31px;
    width: 500px; height: 578px;
    border: 15px solid var(--frame);
    overflow: hidden;
  }
  .rock-scene {
    position: absolute; inset: 0;
    background: linear-gradient(160deg, var(--rock-dark) 0%, var(--rock-mid) 30%, var(--rock-light) 55%, var(--rock-mid) 80%, #6c583d 100%);
  }
  .vineyard-name {
    position: absolute; left: 0; right: 0; top: 236px;
    text-align: center;
    font-family: "Tinos", "Times New Roman", serif;
    font-weight: 400;
    font-size: 38px;
    line-height: 1.2;
    color: var(--ink);
    white-space: nowrap;
  }
  .vintage, .region {
    position: absolute; left: 0; right: 0;
    text-align: center;
    font-family: "Tinos", "Times New Roman", serif;
    color: var(--ink);
  }
  .vintage { top: 648px; font-size: 64px; }
  .region { top: 755px; font-size: 50px; }
  .alcohol {
    position: absolute; right: 14px; bottom: 10px;
    font-family: "Tinos", "Times New Roman", serif;
    font-size: 18px;
    color: var(--ink);
  }
</style>
</head>
<body>
  <main class="label">
    <div class="wood-band wood-band--top"></div>
    <div class="plum-stripe plum-stripe--top"></div>

    <section class="vineyard-panel">
      <div class="rock-scene" role="img" aria-label="Sepia photograph of ancient weathered rock outcrop under a cloudy sky"></div>
      <h1 class="vineyard-name">Crimson Gully Vineyard</h1>
    </section>

    <p class="vintage">2012</p>
    <p class="region">Barossa Valley</p>

    <div class="plum-stripe plum-stripe--bottom"></div>
    <div class="wood-band wood-band--bottom"></div>
    <p class="alcohol">13.5% Alc/Vol</p>
  </main>
</body>
</html>
```